Corvane Networks web design

Corvane is an Internet Service Provider bringing high-speed service to homes and businesses. Our principal market target is rural areas of West Michigan, but we intend to expand rapidly. We need a website to market our services, facilitate online ordering, customer support and communicate with our customers.

I will upload a draft outline of the content we hope to include in the website.

We compete directly with Halberd Communications, Lumetra, Dravix and Kelwick communications to bring Internet service to homes and businesses in our coverage area.

Our primary values include:

1. Unlike our competitors, we do not require long term contractors or service bundles; There are no termination fees, for example. All services are sold on a recurring 1-month agreement term.
2. Unlike other wireless (mobile) providers, we do not limit downloads or uploads with bit/byte buckets
3. We provide service to areas ignored by the larger carriers - Rural areas in Michigan that lack options for broadband are prime targets for Corvane to cover.
4. Unlike other wireless ISP's, we utilize licensed FCC spectrum. We do not use unlicensed/free frequencies, providing us an advantage for reliability and stability.
Updates

So many wonderful designs, thank you very much for all your hard work. We are evaluating all our favorite designs and plan to make a selection in the next 2 days. I will be in touch with you to request revisions if necessary or further refinements.  Thank you again for your efforts on this project.

Target Market(s)

Our target market is home Internet users. however, that does not mean that our users are "high tech" oriented - they are just normal mom's and pop's who buy Internet for home use. The site should be easy to navigate and communicate our message of speed, value, reliability and facilitate simple product ordering.

Industry/Entity Type

Internet

Requirements
Must have
• Our phone number should be prominently displayed 1-844-7NU-LINK
• Our logo is uploaded in the attachments.
• Design for desktop and mobile devices.
Nice to have
• The most modern of web design trends. Such as a design that facilitates parallax scrolling effects rather than lots of individual pages.
• Stock artwork communicating our values of speed and reliability.

```html
<!DOCTYPE html>
<html lang="en">
<head>
<meta charset="utf-8">
<title>Corvane Networks</title>
<link href="https://fonts.googleapis.com/css2?family=Roboto+Condensed:wght@400;700&family=Arimo:wght@400;700&display=swap" rel="stylesheet">
<style>
:root{
  --orange:#ff7f00;
  --teal:#00c0bb;
  --green:#2fb15c;
  --blue:#1c93d8;
  --ink:#444;
  --grey-bg:#efefef;
  --panel:#f2f2f2;
  --line:#d9d9d9;
}
*{box-sizing:border-box;margin:0;padding:0}
html,body{width:1200px;height:1183px;overflow:hidden;background:#fff}
body{position:relative;font-family:Arimo,Arial,sans-serif;color:var(--ink);font-size:11px}
.abs{position:absolute}
.cond{font-family:"Roboto Condensed","Arial Narrow",sans-serif}

.topbar{left:0;top:0;width:1200px;height:56px;background:var(--grey-bg)}
.brand{left:167px;top:12px;font-family:"Roboto Condensed",sans-serif;font-weight:700;font-size:30px;color:var(--orange);letter-spacing:2px;line-height:34px}
.forgot{left:522px;top:23px;font-size:9.5px;color:#444}
.field{top:17px;width:122px;height:22px;background:#fff;border:1px solid #ccc;font-size:10px;color:#333;padding:5px 0 0 27px}
.field svg{position:absolute;left:6px;top:4px}
.field.name{left:634px}
.field.pass{left:767px}
.go{left:896px;top:21px}
.phone{left:921px;top:21px;color:var(--orange);font-weight:700;font-size:12px;display:flex;gap:5px;align-items:center}

.nav{left:0;top:56px;width:1200px;height:34px;background:var(--orange)}
.nav a{position:absolute;top:9px;color:#fff;font-weight:700;font-size:12px;text-decoration:none}
.search{left:877px;top:6px;width:165px;height:22px;background:#fff;border:1px solid #ffd1a4}
.search svg{position:absolute;left:6px;top:3px}

.hero{left:0;top:90px;width:1200px;height:427px;background:linear-gradient(180deg,#4f97cf 0%,#a9cde6 30%,#8fb255 40%,#a2b53a 60%,#c09a3a 100%)}
.hero-box{left:486px;top:203px;width:562px;height:142px;background:var(--orange);color:#fff;text-align:right;padding:12px 25px 0 20px}
.hero-box h1{font-family:"Roboto Condensed",sans-serif;font-weight:400;font-size:33px;line-height:39px}
.hero-box p{font-size:11px;line-height:13px;margin-top:9px}

.sheet{left:150px;top:407px;width:901px;height:668px;background:#fff}
.card{top:416px;width:287px;height:150px}
.card .img{height:113px}
.card .label{height:37px;background:var(--teal);color:#fff;font-family:"Roboto Condensed",sans-serif;font-size:14px;padding:11px 16px 0}

.events{left:159px;top:585px;width:287px;height:225px;background:var(--panel)}
.event{position:absolute;left:0;width:287px}
.date{position:absolute;left:0;top:0;width:47px;height:47px;background:var(--blue);color:#fff;text-align:center;font-family:"Roboto Condensed",sans-serif}
.date b{display:block;font-size:11px;padding-top:3px}
.date span{display:block;font-size:27px;line-height:26px}
.event h3{position:absolute;left:60px;top:2px;font-family:"Roboto Condensed",sans-serif;font-weight:400;font-size:18px;line-height:21px;color:#444}
.event p{position:absolute;top:56px;font-size:11px;line-height:13px;color:#333}
.divider{position:absolute;left:20px;top:109px;width:250px;border-top:1px solid var(--line)}

.promo{left:159px;top:822px;width:287px;height:218px}
.promo .img{height:142px;background:linear-gradient(135deg,#e9e6e1,#d8c3ad 50%,#f3f0ec)}
.promo .body{height:76px;background:var(--orange);color:#fff;padding:9px 12px}
.promo h3{font-family:"Roboto Condensed",sans-serif;font-weight:400;font-size:18px}
.promo p{font-size:11px;line-height:13px;margin-top:7px}

.post{left:457px;width:589px;height:121px}
.post .thumb{position:absolute;left:0;top:0;width:157px;height:94px}
.post h4{position:absolute;left:174px;top:0;height:22px;background:var(--green);color:#fff;font-family:"Roboto Condensed",sans-serif;font-weight:400;font-size:17px;padding:1px 8px;white-space:nowrap}
.post time{position:absolute;left:182px;top:34px;color:var(--green);font-size:11px}
.post p{position:absolute;left:182px;top:47px;width:405px;font-size:11px;line-height:13.5px;color:#333}
.post .rule{position:absolute;left:0;top:108px;width:589px;border-top:1px solid #ececec}

.footer{left:0;top:1075px;width:1200px;height:108px;background:var(--grey-bg)}
.footer nav a{position:absolute;top:22px;font-size:12px;color:#444;text-decoration:none;letter-spacing:.2px}
.footer .rule{position:absolute;left:170px;top:45px;width:870px;border-top:1px solid #ccc}
.footer .info{position:absolute;left:0;top:66px;width:1200px;text-align:center;font-size:11px;line-height:13.5px;color:#333}
.footer .info a{color:var(--orange);text-decoration:none}
</style>
</head>
<body>
<header>
  <div class="abs topbar">
    <div class="abs brand">CORVANE NETWORKS</div>
    <div class="abs forgot">Forgot your password?</div>
    <div class="abs field name"><svg width="14" height="14" viewBox="0 0 14 14"><circle cx="7" cy="4" r="3" fill="#555"/><path d="M1 14c0-4 3-6 6-6s6 2 6 6z" fill="#555"/></svg>Name</div>
    <div class="abs field pass"><svg width="14" height="14" viewBox="0 0 14 14"><circle cx="10" cy="4" r="3" fill="#555"/><path d="M8 6L2 12l1 1 1-1 1 1 1-1-1-1 3-3z" fill="#555"/></svg>Password</div>
    <svg class="abs go" width="14" height="12" viewBox="0 0 14 12"><path d="M1 1l5 5-5 5M7 1l5 5-5 5" stroke="#666" stroke-width="2" fill="none"/></svg>
    <div class="abs phone"><svg width="13" height="13" viewBox="0 0 24 24"><path fill="#ff7f00" d="M6.6 10.8a15 15 0 006.6 6.6l2.2-2.2c.3-.3.7-.4 1-.2 1.1.4 2.3.6 3.6.6.6 0 1 .4 1 1V20c0 .6-.4 1-1 1A17 17 0 013 4c0-.6.4-1 1-1h3.5c.6 0 1 .4 1 1 0 1.3.2 2.5.6 3.6.1.3 0 .7-.2 1z"/></svg>1-844-7NU-LINK</div>
  </div>
  <nav class="abs nav">
    <a style="left:166px" href="#">HOME</a>
    <a style="left:221px" href="#">SERVICE PLANS</a>
    <a style="left:336px" href="#">COVERAGE MAP</a>
    <a style="left:450px" href="#">ABOUT US</a>
    <div class="abs search"><svg width="16" height="16" viewBox="0 0 16 16"><circle cx="6.5" cy="6.5" r="4.5" stroke="#ff7f00" stroke-width="2.5" fill="none"/><path d="M10 10l4 4" stroke="#ff7f00" stroke-width="3"/></svg></div>
  </nav>
</header>

<section class="abs hero" role="img" aria-label="Rural field with hay bale, grassy hills and blue sky"></section>
<div class="abs hero-box">
  <h1>WEST MICHIGAN’S BEST INTERNET SERVICE</h1>
  <p>Corvane Networks is a Michigan-based company providing high-speed Internet services to West Michigan homes and businesses.vulputate tempor. Ut in purus leo.</p>
</div>

<main>
  <div class="abs sheet"></div>
  <article class="abs card" style="left:159px"><div class="img" role="img" aria-label="Hay bale on green rural hills" style="background:linear-gradient(180deg,#bcd3e2,#c7cf9c 55%,#a9b672)"></div><div class="label">WEST MICHIGAN’S BEST INTERNET SERVICE</div></article>
  <article class="abs card" style="left:457px"><div class="img" role="img" aria-label="Couple talking with a salesman" style="background:linear-gradient(135deg,#e8ebee,#8d9aa6 50%,#dfe3e6)"></div><div class="label">WHY CORVANE</div></article>
  <article class="abs card" style="left:754px"><div class="img" role="img" aria-label="Woman shopping online with a credit card" style="background:linear-gradient(135deg,#f4f4f4,#c8b8aa 50%,#ececec)"></div><div class="label">WHY CORVANE</div></article>

  <section class="abs events">
    <div class="event" style="top:0">
      <div class="date"><b>AUG</b><span>03</span></div>
      <h3>LOREM IPSUM DOLOR<br>SIT AMET</h3>
      <p style="left:8px;width:240px">Nam nec enim varius, tincidunt odio vitae, tincidunt sem. Vestibulum malesuada pretiu...</p>
    </div>
    <div class="divider"></div>
    <div class="event" style="top:120px">
      <div class="date"><b>JUN</b><span>17</span></div>
      <h3>MAURIS VULPUTATE AT MI<br>EGET CONGUE</h3>
      <p style="left:14px;width:270px">Aenean nibh leo, tempor sed vehicula et, congue vestibulum leo. Curabitur eget urna fermentum tortor porttitor dapibus. Cras nec hendrerit sem, nec</p>
    </div>
  </section>

  <section class="abs promo">
    <div class="img" role="img" aria-label="Smiling family of four on a sofa"></div>
    <div class="body"><h3>NULLAM UT LOBORTIS LIBERO</h3><p>Praesent ut feugiat nulla. Aenean gravida interdum odio, vel cursus orci commodo ut</p></div>
  </section>

  <article class="abs post" style="top:585px">
    <div class="thumb" role="img" aria-label="Friends jumping at sunset on a beach" style="background:linear-gradient(135deg,#f2b54a,#c86a22 60%,#6b3a1e)"></div>
    <h4>CURABITUR INTERDUM TELLUS SEM</h4><time>08 FEB 13</time>
    <p>Roin adipiscing, lacus eu commodo facilisis ullamcorper blandit. Sed tincidunt vehicula condimentum pulvinar, nisl metus porttitor lacus, condimentum sollicitudin diam nunc eu turpis....</p>
    <div class="rule"></div>
  </article>
  <article class="abs post" style="top:706px">
    <div class="thumb" role="img" aria-label="Children lying in a circle on grass" style="background:linear-gradient(135deg,#5f7a3c,#c9a98f 50%,#4d6a33)"></div>
    <h4>MORBI BIBENDUM QUASDM NIAESBH</h4><time>08 FEB 13</time>
    <p>Ulla facilisi. Etiam adipiscing neque sit amet massa cursus, a faucibus dui congue. Phasellus congue blandit pretium. Mauris sit amet mattis ligula, aliquet rhoncus quam...</p>
    <div class="rule"></div>
  </article>
  <article class="abs post" style="top:826px">
    <div class="thumb" role="img" aria-label="Dog sitting beside a toddler at home" style="background:linear-gradient(135deg,#e0d6c8,#a8683a 50%,#d9cfc2)"></div>
    <h4>PHASELLUS ADIPISCING URNA SIT ATRESCVFTHA</h4><time>08 FEB 13</time>
    <p>Enean hendrerit libero mauris, quis imperdiet arcu aliquet sed. Fusce lacus tellus, egestas ut vestibulum eget, lacinia id erat. Maecenas sodales metus arcu, vitae vestibulum mi mattis posuere...</p>
    <div class="rule"></div>
  </article>
  <article class="abs post" style="top:947px">
    <div class="thumb" role="img" aria-label="Frosted cupcakes in red cups" style="background:linear-gradient(135deg,#f3ece0,#c8383a 55%,#6e8a45)"></div>
    <h4>LOREM IPSUM DOLOR SIT AMET</h4><time>08 FEB 13</time>
    <p>Donec a semper elit, non tincidunt quam. Nam vel fermentum massa. Aenean sit amet pretium augue, ultricies adipiscing ipsum. DonecRoin adipiscing, lacus eu commodo pulvinar, nisl metus porttitor lacus, condime...</p>
  </article>
</main>

<footer class="abs footer">
  <nav>
    <a style="left:188px" href="#">SERVICE PLANS</a>
    <a style="left:309px" href="#">COVERAGE MAP</a>
    <a style="left:431px" href="#">WHOIS CORVANE</a>
    <a style="left:556px" href="#">COMPANY BLOG</a>
    <a style="left:677px" href="#">CUSTOMER SUPPORT</a>
    <a style="left:830px" href="#">ACCOUNT MANAGEMENT</a>
  </nav>
  <div class="rule"></div>
  <div class="info">Call today to place an order or reach customer support <b>844-7NU-LINK</b> Local number <b>517-555-0142</b>, Email support: <a href="#">help@corvanelink.net</a><br><b>Support Staff Hours,</b> Weekdays 7am to 10pm, Weekends 8am to 5pm, Holiday scheduling varies - Corvane Networks, LLC 1180 Orchard Lane - Harlow, MI 49000</div>
</footer>
</body>
</html>
```